40th birthday party invitation

Las Vegas theme birthday party for my wife's 40th (Judith) at our property, Belvora Manor (some photos attached - see www.quenby-estate.com.au for more photos) - which is a (pretend) casino for the night.
Basic double-sided card, photo-shop expert needed because: -
Side 1: we're thinking of dropping our house onto a photo of the strip - or dropping the top of Orlon's Citadel (photo example attached) onto our property (and change words to "Judys Citadel").
Maybe also take the famous "Greetings from Pinecrest Basin" (photo example attached) and changing to "Greetings from Jude Basin, Tallai".
Ultimately, we're open to ideas.
Key info:
14 December 2013 @ 6pm
Judith's 40th Birthday Celebration
Side 2: Perhaps a collage of Vegas photos and one of Judith. Again, very open to ideas.
Key info:
Dress Code: Las Vegas Theme
Where: Judys Citadel, 52 Belvora Crescent, Tallai, Qld, 4213

```html
<!DOCTYPE html>
<html lang="en">
<head>
<meta charset="utf-8">
<title>Judith's 40th Birthday Celebration</title>
<link rel="stylesheet" href="https://fonts.googleapis.com/css2?family=Pinyon+Script&family=Oswald:wght@500&family=Roboto+Slab:wght@700&display=swap">
<style>
  :root {
    --sky-top: #0d1f7a;
    --sky-mid: #2a3fb8;
    --glow-pink: #e0418f;
    --glow-magenta: #b52a80;
    --water: #4a1e5c;
    --water-deep: #2a1238;
    --building-gold: #c98a3a;
    --dress-red: #d8332f;
    --dress-deep: #8f1a1a;
    --card-cream: #f2ece0;
    --title-ink: #ecebf7;
    --info-ink: #c4e2f7;
  }
  * { margin: 0; padding: 0; box-sizing: border-box; }
  html, body { width: 1200px; height: 800px; overflow: hidden; background: #ffffff; }
  .invitation {
    position: relative;
    width: 1200px;
    height: 800px;
    overflow: hidden;
  }
  .night-strip-scene {
    position: absolute;
    inset: 0;
    background:
      radial-gradient(ellipse 420px 260px at 900px 330px, rgba(201,138,58,0.75), transparent 70%),
      radial-gradient(ellipse 520px 200px at 620px 500px, rgba(224,65,143,0.85), transparent 75%),
      linear-gradient(180deg, var(--sky-top) 0%, var(--sky-mid) 32%, var(--glow-magenta) 55%, var(--glow-pink) 68%, var(--water) 80%, var(--water-deep) 100%);
  }
  .guest-of-honour-photo {
    position: absolute;
    left: 10px;
    top: 40px;
    width: 345px;
    height: 760px;
    border-radius: 150px 150px 0 0;
    background:
      radial-gradient(ellipse 90px 120px at 180px 200px, rgba(120,80,60,0.55), transparent 80%),
      linear-gradient(180deg, rgba(216,51,47,0.0) 0%, rgba(120,70,50,0.6) 18%, rgba(216,51,47,0.85) 45%, var(--dress-red) 70%, var(--dress-deep) 100%);
  }
  .playing-cards-photo {
    position: absolute;
    left: 0;
    top: 610px;
    width: 540px;
    height: 190px;
    background: linear-gradient(90deg, var(--card-cream) 0%, rgba(242,236,224,0.85) 55%, rgba(242,236,224,0) 100%);
    clip-path: polygon(0 20%, 70% 0, 100% 60%, 100% 100%, 0 100%);
  }
  .event-title {
    position: absolute;
    left: 200px;
    top: 30px;
    width: 940px;
    text-align: center;
    font-family: "Pinyon Script", cursive;
    font-size: 50px;
    line-height: 1.2;
    color: var(--title-ink);
  }
  .event-date {
    position: absolute;
    left: 400px;
    top: 340px;
    width: 700px;
    text-align: center;
    font-family: "Oswald", sans-serif;
    font-weight: 500;
    font-size: 66px;
    line-height: 1.2;
    color: var(--info-ink);
  }
  .event-dress-code {
    position: absolute;
    left: 400px;
    top: 478px;
    width: 675px;
    text-align: center;
    font-family: "Roboto Slab", serif;
    font-weight: 700;
    font-size: 33px;
    line-height: 1.2;
    color: var(--info-ink);
  }
  .event-venue {
    position: absolute;
    left: 360px;
    top: 565px;
    width: 830px;
    text-align: center;
    font-family: "Roboto Slab", serif;
    font-weight: 700;
    font-size: 24px;
    line-height: 1.3;
    color: var(--info-ink);
  }
</style>
</head>
<body>
  <main class="invitation">
    <div class="night-strip-scene" role="img" aria-label="Night photograph of a grand casino hotel lit in gold behind pink illuminated fountains over a lake"></div>
    <div class="playing-cards-photo" role="img" aria-label="Fanned playing cards spread across the lower left corner"></div>
    <div class="guest-of-honour-photo" role="img" aria-label="Photograph of Judith in a red one-shoulder satin dress and red fascinator holding a champagne glass"></div>

    <h1 class="event-title">Judith’s 40th Birthday Celebration!</h1>
    <p class="event-date">14 December 2013 @ 6pm</p>
    <p class="event-dress-code">Dress Code: Las Vegas Theme</p>
    <p class="event-venue">Where: Judys Citadel, 52 Belvora Crescent, Tallai, Qld 4213</p>
  </main>
</body>
</html>
```